I'm looking for strong image and design for the first book in a series titled "Bernard Whitcombe On A Voyage Through Our Convictions" subtitle "Finding a Footing in Living"; although it's about beliefs, I'm not look for an ethereal feel as the first book is about how our beliefs impact our actions and expectations. I'm a published philosopher and keen on branding my name for professional purposes hence the use of my name :) The book will initially be an e-book but I will follow up with a paperback soon afterwards. My website http://bernardwhitcombe-example.com/ may provide some help on me and my projects. Thanks, Bern

Target Market(s)

Graduates and corporate folk who tend to lose their way in the systems.

Logo Text

Bernard Whitcombe on Convictions

Font styles to use
Sans Serif

Colors

Designer to choose colors to be used in the design.

Requirements
Must have
• Needless to say, but impact.
Nice to have
• Strong colours
Should not have
• Religious imagery; the book is philosophical and leans into living in this world.

```html
<!DOCTYPE html>
<html lang="en">
<head>
<meta charset="utf-8">
<title>Bernard Whitcombe On A Voyage Through Our Convictions — Cover</title>
<link rel="stylesheet" href="https://fonts.googleapis.com/css2?family=Russo+One&display=swap">
<style>
  :root {
    --page-bg: #ffffff;
    --cover-black: #141414;
    --portrait-dark: #2a2a2a;
    --portrait-mid: #8a8a8a;
    --portrait-light: #c9c9c9;
    --silver-light: #f2f2f2;
    --silver-mid: #a9a9a9;
    --silver-dark: #5e5e5e;
  }
  * { margin: 0; padding: 0; box-sizing: border-box; }
  html, body {
    width: 1090px;
    height: 1200px;
    overflow: hidden;
    background: var(--page-bg);
  }
  .canvas {
    position: relative;
    width: 1090px;
    height: 1200px;
    background: var(--page-bg);
  }
  .cover {
    position: absolute;
    left: 165px;
    top: 80px;
    width: 760px;
    height: 1040px;
    background: var(--cover-black);
    overflow: hidden;
  }
  .cover__portrait {
    position: absolute;
    top: 0;
    right: 0;
    width: 282px;
    height: 100%;
    background:
      radial-gradient(ellipse 70% 40% at 25% 42%, var(--portrait-light) 0%, var(--portrait-mid) 55%, transparent 100%),
      linear-gradient(90deg, var(--portrait-mid) 0%, var(--portrait-dark) 70%, #1c1c1c 100%);
  }
  .cover__text {
    position: absolute;
    left: 0;
    top: 0;
    width: 462px;
    height: 100%;
    text-align: right;
    font-family: "Russo One", sans-serif;
    text-transform: uppercase;
  }
  .metal {
    color: var(--silver-mid);
    background: linear-gradient(180deg, var(--silver-light) 0%, var(--silver-mid) 45%, var(--silver-dark) 55%, var(--silver-light) 100%);
    background-size: 100% 1.1em;
    -webkit-background-clip: text;
    background-clip: text;
    -webkit-text-fill-color: transparent;
  }
  .cover__title {
    position: absolute;
    right: 0;
    top: 18px;
    font-size: 60px;
    line-height: 0.99;
    letter-spacing: -0.5px;
    font-weight: 400;
  }
  .cover__subtitle {
    position: absolute;
    right: 0;
    top: 742px;
    font-size: 42px;
    line-height: 1.05;
    font-weight: 400;
  }
  .cover__subtitle span, .cover__title span { display: block; }
</style>
</head>
<body>
<div class="canvas">
  <div class="cover">
    <div class="cover__portrait" role="img" aria-label="Black and white close-up portrait of a young woman with long straight hair, half face visible"></div>
    <div class="cover__text">
      <h1 class="cover__title metal">
        <span>Bern-</span>
        <span>ard</span>
        <span>Whit-</span>
        <span>combe</span>
        <span>On A</span>
        <span>Voyage</span>
        <span>Through</span>
        <span>Our</span>
        <span>Convic-</span>
        <span>tions</span>
      </h1>
      <p class="cover__subtitle metal">
        <span>Finding</span>
        <span>A Footing</span>
        <span>In</span>
        <span>Living</span>
      </p>
    </div>
  </div>
</div>
</body>
</html>
```